Business Card for Professional Domainer

Require a business card design for an Individual Person who is a Professional Domainer.

Who is a Professional Domainer?
A domainer is someone who earns a profit buying and selling domain names.
Professional Domainer are the ones who do this on a full time basis.

So we require the business card design to be related to the above work.

There is no company or any logo currently, as the card is required for an Individual Person.

Business Card required to mention following details:

1. Full Name of the Person (Ex: Marisol Kettner)
2. Education Qualification (Ex: B.Tech Computer Science)
3. Mobile Number (Ex: +71 4837160295)
4. Website (Ex: www.trelmixo.com)
5. Email (Ex: hello@trelmixo.com)

Positioning of the details:

1. Mobile Number should be placed to Right Top Corner
2. Education Qualification should be just below Full Name
3. Website and Email should be on Bottom Part, on a bar at the bottom

It's important to include images related to the nature of work (Domaining) in the card design.
A good related image would be great. Image should be either in background or as a logo.
The image should be focus of the business card, and shoudl speak out on itself.
Anyone looking at the card should understand at one look what work is being done.
So kindly use images in the design which are highly relevant to domaining and domain names.

Along with the image, it's also good if you use the word "Professional Domainer" anywhere in the design.
Maybe along with the image or somewhere it would fit. These words would be like company name.
So please try to use these words "Professional Domainer" in the design, as it will help a lot.

Colors: Blue, Red, Green

We like these colors, but you are free to use any color which would be good for the design.

Card design should be according to Quornalex specs:

Document Trim Size = 91 x 55 mm | 1075 x 650 pixels
Full Bleed Size = 94 x 58 mm | 1110 x 685 pixels

Last thing, the business card should look professional and clean.
People should know that the person is a Professional Domainer at one look of the card.

Thank You and All the Best :)

Message to the the designers working on this project:

We have now guaranteed this project. This means, we will 100% choose a design and award the project to the one we like the best. So kindly submit your best designs before Wednesday, 3 July 2013. After that we are going to finalize the project and award to the best one. So please hurry up so that you are not too late. Thank You and All the Best!

```html
<!DOCTYPE html>
<html lang="en">
<head>
<meta charset="utf-8">
<title>Professional Domainer – Business Cards</title>
<link rel="stylesheet" href="https://fonts.googleapis.com/css2?family=Open+Sans:wght@400;600;700&family=Roboto+Condensed:wght@700&display=swap">
<style>
  :root {
    --page: #eceff2;
    --sky: #2fa3e3;
    --sky-light: #bfe3f7;
    --sky-deep: #0b78c6;
    --globe-mid: #3f7fd4;
    --globe-deep: #163f96;
    --navy: #2a3f7e;
    --ink: #333333;
    --red: #e1222b;
    --green: #6cc6a0;
    --white: #ffffff;
  }
  * { margin: 0; padding: 0; box-sizing: border-box; }
  html, body { width: 1094px; height: 1200px; overflow: hidden; }
  body { background: var(--page); font-family: "Open Sans", Arial, sans-serif; position: relative; }

  .card {
    position: absolute; left: 124px; width: 787px; height: 477px;
    overflow: hidden; background: var(--white);
    box-shadow: 0 4px 14px rgba(0,0,0,.18);
  }
  .card--front { top: 74px; }
  .card--back { top: 626px; }

  .card__backdrop { position: absolute; inset: 0; }
  .card--front .card__backdrop {
    background: radial-gradient(ellipse 520px 420px at 0 0, var(--sky) 0%, #7cc7f0 45%, rgba(255,255,255,0) 100%);
  }
  .card--back .card__backdrop {
    background: radial-gradient(ellipse 620px 480px at 100% 0, var(--sky) 0%, #8ad0f3 50%, rgba(255,255,255,0) 100%);
  }
  .card__waves { position: absolute; inset: 0; }

  .globe-art {
    position: absolute; border-radius: 50%;
    background: radial-gradient(circle at 40% 38%, var(--globe-mid) 0%, var(--globe-deep) 100%);
  }

  .phone {
    position: absolute; font-family: "Roboto Condensed", "Arial Narrow", sans-serif;
    font-weight: 700; font-size: 26px; color: var(--red);
    display: flex; align-items: center; gap: 10px; line-height: 1;
  }
  .phone svg { flex: none; }
  .title {
    position: absolute; font-weight: 700; font-size: 27px; color: var(--red);
    line-height: 1; white-space: nowrap;
  }
  .name { position: absolute; font-weight: 600; font-size: 24px; line-height: 1; white-space: nowrap; }
  .degree { position: absolute; font-weight: 400; font-size: 20px; line-height: 1; white-space: nowrap; }
  .contact {
    position: absolute; font-size: 24px; line-height: 1; white-space: nowrap;
    display: flex; flex-direction: column; align-items: flex-end;
  }
  .contact__row { display: flex; align-items: center; gap: 14px; }

  .card--front .phone { right: 80px; top: 48px; }
  .card--front .title { left: 222px; top: 127px; }
  .card--front .name { left: 298px; top: 190px; color: var(--navy); }
  .card--front .degree { left: 263px; top: 229px; color: var(--navy); }
  .card--front .contact { right: 81px; top: 387px; gap: 8px; color: var(--navy); }
  .card--front .globe-art { left: 288px; top: 319px; width: 140px; height: 134px; }

  .card--back .phone { right: 75px; top: 57px; }
  .card--back .title { left: 78px; top: 107px; }
  .card--back .name { left: 78px; top: 173px; color: var(--ink); font-weight: 700; }
  .card--back .degree { left: 78px; top: 208px; color: var(--ink); }
  .card--back .contact { right: 75px; top: 367px; gap: 7px; color: var(--ink); }
  .card--back .globe-art { left: 111px; top: 270px; width: 150px; height: 146px; }
</style>
</head>
<body>

<section class="card card--front">
  <div class="card__backdrop" role="img" aria-label="Faint world map with connection lines on a blue gradient"></div>
  <svg class="card__waves" viewBox="0 0 787 477" preserveAspectRatio="none" aria-hidden="true">
    <path d="M0 300 C120 430 260 470 420 410 C560 355 680 300 787 330 L787 477 L0 477 Z" fill="#d8effb"/>
    <path d="M0 330 C110 440 270 460 420 400 C560 345 690 290 787 320 L787 352 C690 320 570 370 430 425 C280 480 120 460 0 380 Z" fill="var(--sky-deep)" opacity=".85"/>
    <path d="M0 370 C130 470 290 470 440 420 C580 372 700 330 787 350 L787 372 C700 350 580 395 450 440 C300 492 130 480 0 400 Z" fill="var(--sky)"/>
    <path d="M0 395 C140 480 300 490 460 445 C600 405 700 380 787 395 L787 477 L0 477 Z" fill="#f1f9fe"/>
    <path d="M0 230 C30 330 140 400 290 390 C430 380 560 280 690 262 C730 257 760 265 787 280" fill="none" stroke="var(--green)" stroke-width="7"/>
    <path d="M560 330 C640 300 720 310 787 345" fill="none" stroke="#7fd0f4" stroke-width="10" opacity=".8"/>
  </svg>

  <div class="phone">
    <svg width="18" height="22" viewBox="0 0 18 22" aria-hidden="true"><path d="M4 1 L7 6 L5 8 C6 12 8 15 11 17 L13 15 L17 18 L14 21 C7 20 1 12 1 4 Z" fill="var(--red)"/></svg>
    <span>+71 4837160295</span>
  </div>
  <h1 class="title">PROFESSIONAL DOMAINER</h1>
  <p class="name">Marisol Kettner</p>
  <p class="degree">B.Tech Computer Science</p>
  <div class="globe-art" role="img" aria-label="Illustration: globe wrapped by a web address bar with a pointing hand cursor"></div>
  <div class="contact">
    <span>www.trelmixo.com</span>
    <span>hello@trelmixo.com</span>
  </div>
</section>

<section class="card card--back">
  <div class="card__backdrop" role="img" aria-label="Faint world map with connection lines on a blue gradient"></div>
  <svg class="card__waves" viewBox="0 0 787 477" preserveAspectRatio="none" aria-hidden="true">
    <path d="M0 250 C70 370 170 400 300 380 C460 355 600 270 787 270 L787 477 L0 477 Z" fill="#d8effb"/>
    <path d="M0 275 C80 390 200 410 330 390 C480 366 620 290 787 300 L787 335 C620 320 490 395 340 420 C200 440 80 420 0 330 Z" fill="var(--sky-deep)" opacity=".85"/>
    <path d="M0 330 C100 430 230 440 360 420 C520 395 650 340 787 350 L787 372 C650 365 530 420 370 445 C230 466 100 455 0 370 Z" fill="var(--sky)"/>
    <path d="M0 380 C120 460 260 470 400 452 C560 430 680 400 787 405 L787 477 L0 477 Z" fill="#f3faff"/>
    <path d="M0 228 C50 340 160 385 290 372 C430 358 560 285 690 262 C730 256 760 258 787 266" fill="none" stroke="var(--red)" stroke-width="6"/>
  </svg>

  <div class="phone">
    <svg width="22" height="30" viewBox="0 0 22 30" aria-hidden="true"><rect x="1.5" y="1.5" width="19" height="27" rx="3" fill="none" stroke="var(--red)" stroke-width="3"/><rect x="5" y="5" width="12" height="16" fill="var(--red)"/><circle cx="11" cy="24.5" r="1.6" fill="var(--red)"/></svg>
    <span>+71 4837160295</span>
  </div>
  <h2 class="title">PROFESSIONAL DOMAINER</h2>
  <p class="name">Marisol Kettner</p>
  <p class="degree">B.Tech Computer Science</p>
  <div class="globe-art" role="img" aria-label="Illustration: globe wrapped by a web address bar with an arrow cursor"></div>
  <div class="contact">
    <div class="contact__row">
      <svg width="22" height="22" viewBox="0 0 22 22" aria-hidden="true"><g fill="none" stroke="var(--red)" stroke-width="1.6"><circle cx="11" cy="11" r="9.5"/><ellipse cx="11" cy="11" rx="4.5" ry="9.5"/><path d="M1.5 11 H20.5 M3 6 H19 M3 16 H19"/></g></svg>
      <span>www.trelmixo.com</span>
    </div>
    <div class="contact__row">
      <svg width="22" height="16" viewBox="0 0 22 16" aria-hidden="true"><g fill="none" stroke="var(--red)" stroke-width="1.6"><rect x="1" y="1" width="20" height="14"/><path d="M1 1 L11 9 L21 1"/></g></svg>
      <span>hello@trelmixo.com</span>
    </div>
  </div>
</section>

</body>
</html>
```